We need a logo for our business which is a dental clinic (i.e. dentistry).
We would lilke designs using the colour blue, green and black incorporating the words Corvasta Dental, possibly a smile or a tooth image can be considered for incorporation in the logo.

Industry/Entity Type

Dental

```html
<!DOCTYPE html>
<html lang="en">
<head>
<meta charset="utf-8">
<title>Corvasta Dental – Business Card</title>
<link rel="stylesheet" href="https://fonts.googleapis.com/css2?family=Cantarell&family=Open+Sans:wght@400&display=swap">
<style>
  :root {
    --card-white: #ffffff;
    --brand-blue: #2aa9e0;
    --brand-green: #8cc63f;
    --deep-navy: #272361;
    --text-grey: #555555;
    --contact-white: #ffffff;
    --divider: #e6e6ee;
  }
  * { margin: 0; padding: 0; box-sizing: border-box; }
  html, body {
    width: 1200px;
    height: 686px;
    overflow: hidden;
    background: var(--card-white);
  }
  .card {
    position: relative;
    width: 1200px;
    height: 686px;
    background: var(--card-white);
    overflow: hidden;
  }
  .card-swoosh {
    position: absolute;
    inset: 0;
    width: 1200px;
    height: 686px;
  }
  .swoosh-fill { fill: var(--deep-navy); }
  .swoosh-edge {
    fill: none;
    stroke: var(--brand-green);
    stroke-width: 11;
  }
  .practitioner {
    position: absolute;
    right: 40px;
    top: 48px;
    text-align: right;
  }
  .practitioner-name {
    font-family: "Cantarell", sans-serif;
    font-size: 41px;
    line-height: 1.1;
    color: var(--brand-blue);
  }
  .practitioner-role {
    font-family: "Open Sans", sans-serif;
    font-size: 25px;
    line-height: 1.4;
    margin-top: 10px;
    margin-right: 3px;
    color: var(--text-grey);
  }
  .clinic-lockup {
    position: absolute;
    left: 0;
    right: 0;
    top: 256px;
    display: flex;
    align-items: center;
    justify-content: center;
    gap: 20px;
    padding-right: 70px;
  }
  .clinic-mark {
    width: 26px;
    height: 26px;
    border-radius: 50%;
    background: var(--brand-green);
    flex: none;
  }
  .clinic-name {
    font-family: "Cantarell", sans-serif;
    font-weight: 400;
    font-size: 80px;
    line-height: 1;
    color: var(--brand-blue);
    white-space: nowrap;
  }
  .contact-bar {
    position: absolute;
    left: 138px;
    top: 614px;
    display: flex;
    align-items: center;
    font-family: "Open Sans", sans-serif;
    font-size: 28px;
    color: var(--contact-white);
    white-space: nowrap;
  }
  .contact-divider {
    display: block;
    width: 5px;
    height: 56px;
    background: var(--divider);
    margin: 0 24px;
  }
</style>
</head>
<body>
  <div class="card">
    <svg class="card-swoosh" viewBox="0 0 1200 686" aria-hidden="true">
      <path class="swoosh-fill" d="M0,343 C210,515 420,575 560,571 C800,565 1080,420 1200,192 L1200,686 L0,686 Z"/>
      <path class="swoosh-edge" d="M0,343 C210,515 420,575 560,571 C800,565 1080,420 1200,192"/>
    </svg>

    <div class="practitioner">
      <p class="practitioner-name">Dr. Name</p>
      <p class="practitioner-role">Dentist</p>
    </div>

    <div class="clinic-lockup">
      <span class="clinic-mark" aria-hidden="true"></span>
      <h1 class="clinic-name">Corvasta Dental</h1>
    </div>

    <div class="contact-bar">
      <span class="contact-phone">Ph: xxx xxx xxx</span>
      <span class="contact-divider"></span>
      <span class="contact-email">hello@corvastadental.com</span>
      <span class="contact-divider"></span>
      <span class="contact-address">Address:</span>
    </div>
  </div>
</body>
</html>
```